HARBORLINE AUTO GLASS

Mobile Glass Shop:

1) Windshield REPAIR 2)Windshield replacment 3) Rear Windshield Replacment 4) Side Window Replacment 5) car window replacment 6) Power Window Repair.

Schedual a service within 24 hour with one of our certified technicians.

See "brightvane auto repair" web site for referance on the nature of our buisness and service. www.brightvane-example.com

```html
<!DOCTYPE html>
<html lang="en">
<head>
<meta charset="utf-8">
<title>Harborline Auto Glass – About Us</title>
<link href="https://fonts.googleapis.com/css2?family=Poppins:wght@400;500;600;700;800&display=swap" rel="stylesheet">
<style>
:root{
  --blue:#1e74c8;
  --blue-dark:#145a9e;
  --ink:#1c2127;
  --text:#555b63;
  --muted:#8a9099;
  --dark:#1b1f24;
  --dark-2:#262b31;
  --white:#ffffff;
  --light:#f3f5f8;
  --star:#f5b400;
}
*{box-sizing:border-box;margin:0;padding:0}
html,body{width:1200px;height:3324px;overflow:hidden}
body{font-family:'Poppins',sans-serif;color:var(--text);background:var(--white);position:relative}
.abs{position:absolute}

/* header */
.site-header{position:absolute;top:0;left:0;width:1200px;height:140px;background:var(--white)}
.brand{position:absolute;left:44px;top:34px;display:flex;align-items:center;gap:12px}
.brand-mark{width:58px;height:58px;background:var(--blue)}
.brand-name{font-weight:800;color:var(--ink);line-height:1.05;font-size:24px}
.brand-name small{display:block;font-size:14px;letter-spacing:3px;font-weight:800}
.main-nav{position:absolute;left:390px;top:58px;display:flex;gap:30px;font-size:15px;color:var(--ink);font-weight:500;white-space:nowrap}
.main-nav .active{color:var(--blue);position:relative}
.main-nav .active::after{content:"";position:absolute;left:0;right:0;bottom:-10px;height:3px;background:var(--blue)}
.call-box{position:absolute;right:44px;top:40px;display:flex;align-items:center;gap:12px}
.call-icon{width:44px;height:44px;border-radius:50%;border:2px solid var(--blue);display:flex;align-items:center;justify-content:center;flex:none}
.call-label{font-size:12px;font-weight:600;color:var(--ink);letter-spacing:1px}
.call-number{font-size:21px;font-weight:700;color:var(--blue);line-height:1.1;white-space:nowrap}

/* hero */
.hero{position:absolute;top:140px;left:0;width:1200px;height:740px;background:linear-gradient(110deg,#cfd4da 0%,#9aa2ab 35%,#5b636c 65%,#2e343b 100%)}
.hero-title{position:absolute;left:92px;top:350px;font-size:46px;font-weight:700;color:var(--white);letter-spacing:1px}
.hero-wave{position:absolute;left:0;top:640px}

/* about */
.about-art{position:absolute;left:110px;top:930px;width:430px;height:520px;border-radius:8px;background:radial-gradient(ellipse at center,#f2f4f7 0%,#d8e6f5 55%,#b8cfe8 100%)}
.about-copy{position:absolute;left:620px;top:915px;width:500px}
.section-kicker{font-size:30px;font-weight:700;color:var(--ink)}
.about-title{font-size:30px;font-weight:600;color:var(--ink);margin:44px 0 16px}
.about-title span{color:var(--blue)}
.about-copy p{font-size:15px;line-height:1.75;margin-bottom:22px}

/* stats */
.stats-band{position:absolute;top:1540px;left:0;width:1200px;height:470px;background:linear-gradient(180deg,var(--dark) 0%,var(--dark-2) 100%)}
.stat{position:absolute;top:70px;width:240px;text-align:center;color:var(--white);font-weight:600;font-size:17px;line-height:1.4}
.stat svg{display:block;margin:0 auto 18px}

/* team */
.team-panel{position:absolute;top:1820px;left:78px;width:1044px;height:480px;background:var(--white);box-shadow:0 10px 30px rgba(0,0,0,.08)}
.section-title{text-align:center;font-size:34px;font-weight:700;color:var(--ink);letter-spacing:.5px}
.team-panel .section-title{margin-top:42px}
.team-grid{position:absolute;left:22px;top:128px;display:flex;gap:24px}
.member{width:232px;text-align:center}
.member-photo{width:232px;height:262px;background:linear-gradient(160deg,#7c8794 0%,#2f5e9c 55%,#1f3f6e 100%)}
.member-name{margin-top:22px;font-size:17px;font-weight:600;color:var(--ink)}
.dots{display:flex;gap:6px;justify-content:center}
.dots i{display:block;width:10px;height:4px;background:#c7ccd3;border-radius:2px}
.dots i.on{width:22px;background:var(--blue)}

/* reviews */
.reviews{position:absolute;top:2320px;left:0;width:1200px;height:480px;background:linear-gradient(180deg,#fff 0%,#f2f4f7 100%)}
.reviews .section-title{margin-top:22px}
.section-sub{text-align:center;font-size:14px;letter-spacing:2px;color:var(--muted);margin-top:4px}
.review{position:absolute;top:110px;width:490px;height:290px}
.review-card{position:absolute;left:80px;top:0;width:410px;height:290px;background:var(--white);border-radius:10px;box-shadow:0 8px 26px rgba(0,0,0,.09);padding:36px 30px 0 120px}
.review-photo{position:absolute;left:0;top:48px;width:180px;height:200px;z-index:2;background:linear-gradient(160deg,#a0a8b2,#4b5866)}
.quote{font-size:40px;font-weight:800;color:var(--ink);line-height:.6}
.review-name{font-size:16px;font-weight:600;color:var(--ink);margin-top:10px}
.review-role{font-size:12px;color:var(--muted)}
.review-text{font-size:14px;line-height:1.6;margin-top:18px}
.stars{color:var(--star);font-size:16px;letter-spacing:2px;margin-top:10px}

/* footer */
.site-footer{position:absolute;top:2800px;left:0;width:1200px;height:488px;background:var(--dark);color:#c9ced5}
.footer-brand{position:absolute;left:60px;top:90px;display:flex;align-items:center;gap:12px}
.footer-brand .brand-name{color:var(--white)}
.footer-contact{position:absolute;left:60px;top:210px;font-size:14px;line-height:1.6}
.footer-contact .line{display:flex;align-items:center;gap:10px;margin-bottom:12px}
.footer-contact .big{font-size:22px;font-weight:700;color:var(--white);white-space:nowrap}
.pin-dot{width:30px;height:30px;border-radius:50%;background:var(--blue);flex:none;display:flex;align-items:center;justify-content:center}
.footer-col{position:absolute;top:110px}
.footer-col h4{color:var(--white);font-size:18px;font-weight:600;letter-spacing:2px;margin-bottom:20px}
.footer-col ul{list-style:none;font-size:14px;line-height:2;white-space:nowrap}
.footer-col li::before{content:"›";color:var(--blue);margin-right:8px;font-weight:700}
.field-row{display:flex;gap:12px;margin-bottom:12px}
.field{height:36px;border:1px solid #3b424a;border-radius:3px;font-size:12px;padding:8px 10px;color:#8a9099;flex:1}
.field.area{height:88px}
.submit{display:inline-block;margin-top:6px;background:var(--blue);color:var(--white);font-size:13px;font-weight:600;padding:9px 26px;border-radius:20px;letter-spacing:1px}
.social{position:absolute;left:944px;top:400px;display:flex;gap:12px}
.social i{display:block;width:36px;height:36px;border-radius:50%;background:var(--blue)}
.copyright{position:absolute;top:3288px;left:0;width:1200px;height:36px;background:#111417;color:#8a9099;font-size:12px;line-height:36px;padding-left:60px}
</style>
</head>
<body>

<header class="site-header">
  <div class="brand">
    <div class="brand-mark"></div>
    <div class="brand-name">HARBORLINE<small>AUTO GLASS</small></div>
  </div>
  <nav class="main-nav">
    <span>Home</span><span class="active">About</span><span>Services</span><span>Insurance</span><span>Gallery</span><span>Contact</span>
  </nav>
  <div class="call-box">
    <div class="call-icon">
      <svg width="20" height="20" viewBox="0 0 24 24"><path fill="#1e74c8" d="M6.6 10.8a15.1 15.1 0 0 0 6.6 6.6l2.2-2.2c.3-.3.7-.4 1-.2 1.1.4 2.3.6 3.6.6.6 0 1 .4 1 1V20c0 .6-.4 1-1 1A17 17 0 0 1 3 4c0-.6.4-1 1-1h3.5c.6 0 1 .4 1 1 0 1.3.2 2.5.6 3.6.1.3 0 .7-.2 1z"/></svg>
    </div>
    <div>
      <div class="call-label">CALL US NOW</div>
      <div class="call-number">000 555 010 200</div>
    </div>
  </div>
</header>

<section class="hero" role="img" aria-label="Technician fitting a new windshield using a suction lifter">
  <h1 class="hero-title">ABOUT US</h1>
  <svg class="hero-wave" width="1200" height="100" viewBox="0 0 1200 100">
    <path d="M0 30 Q600 120 1200 30 L1200 100 L0 100 Z" fill="#1e74c8"/>
    <path d="M0 52 Q600 132 1200 52 L1200 100 L0 100 Z" fill="#ffffff"/>
    <circle cx="600" cy="86" r="14" fill="#ffffff"/>
    <path d="M593 84 L600 91 L607 84" stroke="#1e74c8" stroke-width="2.5" fill="none"/>
  </svg>
</section>

<section>
  <div class="about-art" role="img" aria-label="Top view illustration of a white car surrounded by glass service tools with a 20 years experience badge"></div>
  <div class="about-copy">
    <h2 class="section-kicker">ABOUT US</h2>
    <h3 class="about-title">Features For <span>Dream</span></h3>
    <p>Lorem Ipsum is simply dummy text of the printing and typesetting industry has been the industry's standard dummy text ever since the 1500s.</p>
    <p>When an unknown printer took a galley of type and scrambled it to make a type specimen book. It has survived not only five centuries, but also the leap into electronic typesetting, remaining essentially unchanged. It was popularised in the 1960s.</p>
    <p>With the release of Letraset sheets containing Lorem Ipsum passages, and more recently with desktop publishing software like Aldus Page Maker including its electronic typesetting.</p>
  </div>
</section>

<section class="stats-band">
  <div class="stat" style="left:40px">
    <svg width="54" height="54" viewBox="0 0 54 54" fill="none" stroke="#3a8de0" stroke-width="2.5"><rect x="8" y="10" width="38" height="30" rx="2"/><path d="M14 32 L22 24 L30 30 L40 18"/><path d="M20 48 H34 M27 40 V48"/></svg>
    Highest Success<br>Rates
  </div>
  <div class="stat" style="left:320px">
    <svg width="54" height="54" viewBox="0 0 54 54" fill="none" stroke="#3a8de0" stroke-width="2.5"><path d="M8 34 Q10 16 27 16 Q44 16 46 34 Z"/><path d="M6 38 H48"/><circle cx="16" cy="44" r="4"/><circle cx="38" cy="44" r="4"/></svg>
    Experience &amp;<br>Professional
  </div>
  <div class="stat" style="left:632px">
    <svg width="54" height="54" viewBox="0 0 54 54" fill="none" stroke="#3a8de0" stroke-width="2.5"><path d="M12 42 L36 18"/><circle cx="40" cy="14" r="6"/><path d="M42 42 L18 18"/><path d="M10 10 L18 18 M14 8 L20 14"/></svg>
    20Years<br>Of Experience
  </div>
  <div class="stat" style="left:912px">
    <svg width="54" height="54" viewBox="0 0 54 54" fill="none" stroke="#3a8de0" stroke-width="2.5"><circle cx="27" cy="18" r="7"/><path d="M14 44 Q14 30 27 30 Q40 30 40 44"/><circle cx="11" cy="24" r="4"/><circle cx="43" cy="24" r="4"/></svg>
    1000+<br>Happy Clients
  </div>
</section>

<section class="team-panel">
  <h2 class="section-title">MEET OUR TEAM</h2>
  <div class="team-grid">
    <div class="member"><div class="member-photo" role="img" aria-label="Portrait of technician in blue work uniform"></div><div class="member-name">Christopher</div></div>
    <div class="member"><div class="member-photo" role="img" aria-label="Portrait of mechanic in a workshop"></div><div class="member-name">Daniel Weller</div></div>
    <div class="member"><div class="member-photo" role="img" aria-label="Portrait of mechanic holding a wrench"></div><div class="member-name">Robert Malden</div></div>
    <div class="member"><div class="member-photo" role="img" aria-label="Portrait of technician in cap and overalls"></div><div class="member-name">Christopher</div></div>
  </div>
  <div class="dots abs" style="left:0;right:0;top:452px"><i class="on"></i><i></i><i></i></div>
</section>

<section class="reviews">
  <h2 class="section-title">CUSTOMER REVIEWS</h2>
  <p class="section-sub">What Our Clients Say About Us</p>
  <div class="review" style="left:88px">
    <div class="review-photo" role="img" aria-label="Photo of a satisfied customer"></div>
    <div class="review-card">
      <div class="quote">“</div>
      <div class="review-name">Christian Marlow</div>
      <div class="review-role">Director</div>
      <p class="review-text">Lorem ipsum is simply dummy text of the printing and typesetting industry has been the industry's standard.</p>
      <div class="stars">★★★★★</div>
    </div>
  </div>
  <div class="review" style="left:612px">
    <div class="review-photo" role="img" aria-label="Photo of a satisfied customer"></div>
    <div class="review-card">
      <div class="quote">“</div>
      <div class="review-name">Christian Marlow</div>
      <div class="review-role">Director</div>
      <p class="review-text">Lorem ipsum is simply dummy text of the printing and typesetting industry has been the industry's standard.</p>
      <div class="stars">★★★★★</div>
    </div>
  </div>
  <div class="dots abs" style="left:0;right:0;top:420px"><i class="on"></i><i></i><i></i></div>
</section>

<footer class="site-footer">
  <div class="footer-brand">
    <div class="brand-mark"></div>
    <div class="brand-name">HARBORLINE<small>AUTO GLASS</small></div>
  </div>
  <div class="footer-contact">
    <div class="line"><span class="pin-dot"><svg width="14" height="14" viewBox="0 0 24 24"><path fill="#fff" d="M6.6 10.8a15.1 15.1 0 0 0 6.6 6.6l2.2-2.2c.3-.3.7-.4 1-.2 1.1.4 2.3.6 3.6.6.6 0 1 .4 1 1V20c0 .6-.4 1-1 1A17 17 0 0 1 3 4c0-.6.4-1 1-1h3.5c.6 0 1 .4 1 1 0 1.3.2 2.5.6 3.6.1.3 0 .7-.2 1z"/></svg></span><span class="big">000 555 010 200</span></div>
    <div class="line"><span class="pin-dot"><svg width="14" height="14" viewBox="0 0 24 24"><rect x="3" y="6" width="18" height="12" fill="none" stroke="#fff" stroke-width="2"/><path d="M3 6 L12 13 L21 6" fill="none" stroke="#fff" stroke-width="2"/></svg></span>info@harborline-example.com</div>
    <div class="line"><span class="pin-dot"><svg width="14" height="14" viewBox="0 0 24 24"><path fill="#fff" d="M12 2a7 7 0 0 0-7 7c0 5 7 13 7 13s7-8 7-13a7 7 0 0 0-7-7zm0 9.5a2.5 2.5 0 1 1 0-5 2.5 2.5 0 0 1 0 5z"/></svg></span>1234, Harbor Ave<br>#8602, Eastport, CA 12345</div>
  </div>
  <div class="footer-col" style="left:370px">
    <h4>QUICK LINK</h4>
    <ul><li>Home</li><li>About</li><li>Services</li><li>Insurance</li><li>Gallery</li><li>Contact</li></ul>
  </div>
  <div class="footer-col" style="left:530px">
    <h4>SERVICES</h4>
    <ul><li>Windshield Repair</li><li>Windshield Replacement</li><li>Rear Windshield Replacement</li><li>Side Window Replacement</li><li>Car Window Replacement</li><li>Power Window Repair</li></ul>
  </div>
  <div class="footer-col" style="left:808px;width:340px">
    <h4>QUICK CONTACT</h4>
    <div class="field-row"><div class="field">Name*</div><div class="field">Phone*</div><div class="field">Email*</div></div>
    <div class="field area">Message</div>
    <div class="submit">SUBMIT</div>
  </div>
  <div class="social"><i></i><i></i><i></i><i></i></div>
</footer>
<div class="copyright">Copyright © HARBORLINE AUTO GLASS. All Right Reserved</div>

</body>
</html>
```